Modern and strong website design for a Dutch crowdsourcing company
.

We are startup company providing crowdsourcing of administrative and customers service tasks for larger companies and other organizations. We offer cost savings and scale-ability combined with higher quality of execution. We will soon enter the market and need a website that has two major target groups: 1. Our corporate customers 2. The mainly younger crowd executing the tasks on our platform.
The target group of customers are Influencers and decision makers with companies and other organizations in with large administrative and customer service departments. Most information in the startup phase will be targeting this group.
The target group of future crowd workers will be heterogeneous, from students to stay at home mums or night shift workers who want to earn some extra money by performing easy to execute microtasks in the cloud. We will target both Dutch and international workers.

The website must be developed for browsing on a computer but also be optimized for mobile devices and tablets.
The website must be optimized and tested for the major browsers on windows, macOS and mobile devices.

For the minimum requirement for the website see attached wireframes

The present landing page http://thepinegladeloft.com and logo are not reflecting our preferences!
See enclosed a new logo that stands for both the crowdwork (performed for our customers) and the crowd (the pine glade loft).

Target Market(s)

see tekst above.

Industry/Entity Type

Business Service

Coding

Coded - Design and coding required

Number of Pages Required

5+ page

Font styles to use
Sans Serif
Other font styles liked:
• Lato, Open Sans

Colors

Designer to choose colors to be used in the design.

Requirements
Must have
• start devider screen
• home page displaying business and worker information
• a page displaying only info for businesses
• a page displaying only info for workers
• a contact form
• a reviews page
• color scheme from logo
• responsiveness!
Nice to have
• Nice animations
• overlapping blocks, animated on scroll
• lightbox effects if applicable
• animated mobile menu icon and menu itself

```html
<!DOCTYPE html>
<html lang="en">
<head>
<meta charset="utf-8">
<title>The Pine Glade Loft</title>
<link href="https://fonts.googleapis.com/css2?family=Jost:wght@400;500&family=Lato:wght@400;700&display=swap" rel="stylesheet">
<style>
:root{
  --orange:#f07c00;
  --grey:#7b7b7b;
  --grey-dark:#5f5f5f;
  --ink:#2b2b2b;
  --light:#f2f2f2;
  --line:#d9d9d9;
  --black:#111;
  --white:#fff;
}
*{box-sizing:border-box;margin:0;padding:0}
html,body{width:1200px;height:2517px;overflow:hidden}
body{position:relative;background:var(--white);font-family:"Lato",sans-serif;color:var(--ink)}
.abs{position:absolute}
.heading{font-family:"Jost",sans-serif;font-weight:400}

/* top bar */
.topbar{left:640px;top:0;width:560px;height:37px;background:#8a8a8a;display:flex;align-items:center;font-size:13px;color:var(--white)}
.topbar .item{display:flex;align-items:center;gap:12px;padding:0 28px}
.topbar .item+.item{border-left:1px solid #a9a9a9}
.topbar .dot{width:20px;height:20px;border-radius:50%;background:#5c5c5c;display:flex;align-items:center;justify-content:center}
.brand{left:87px;top:17px;width:202px;height:87px;background:var(--white);box-shadow:0 1px 3px rgba(0,0,0,.15);display:flex;align-items:center;gap:10px;padding:0 12px}
.brand .mark{width:26px;height:26px;border-radius:50%;background:var(--orange);flex:none}
.brand .name{font-family:"Jost",sans-serif;font-weight:500;font-size:21px;line-height:1.05;color:var(--grey-dark)}
.nav{left:525px;top:55px;height:62px;display:flex;font-family:"Jost",sans-serif;font-size:14px;color:var(--ink)}
.nav a{color:inherit;text-decoration:none;margin-right:46px;padding-top:12px;height:62px}
.nav a.active{color:var(--orange);border-bottom:3px solid var(--orange)}
.btn{display:flex;align-items:center;justify-content:center;background:var(--orange);color:var(--white);font-family:"Jost",sans-serif;font-size:13px;text-transform:uppercase}
.nav-cta{left:975px;top:55px;width:136px;height:41px;font-size:14px}

/* hero */
.hero{left:0;top:116px;width:1200px;height:518px;background:linear-gradient(100deg,#e9ecef 0%,#cfd6dd 35%,#8d9aae 60%,#d9dde2 100%)}
.hero-caption{left:89px;top:294px;width:487px;height:142px;background:rgba(10,10,10,.88);color:var(--white);padding:22px 30px}
.hero-caption h1{font-size:31px;line-height:1.38;font-weight:400;font-family:"Jost",sans-serif}
.hero-btn{left:117px;top:418px;width:138px;height:38px}

/* section titles */
.section-title{left:0;width:1200px;text-align:center;font-size:36px;color:var(--grey);text-transform:uppercase}
.section-title span{color:var(--orange)}
.divider{left:470px;width:260px;height:20px}
.divider::before,.divider::after{content:"";position:absolute;top:10px;width:110px;height:1px;background:#c4c4c4}
.divider::before{left:0}.divider::after{right:0}
.divider i{position:absolute;left:121px;top:1px;width:18px;height:18px;border-radius:50%;background:#c9c9c9}
.lead{left:134px;width:932px;text-align:center;font-size:13.5px;line-height:25px}

/* split */
.split{left:0;top:909px;width:1200px;height:370px;background:linear-gradient(120deg,#8f8f8f,#6d6d6d)}
.split-orange{left:0;top:909px}
.split-block{width:360px;color:var(--white)}
.split-block h2{font-family:"Jost",sans-serif;font-weight:400;font-size:32px;display:flex;align-items:center;gap:14px;padding-bottom:14px;border-bottom:2px solid rgba(255,255,255,.9);width:46px;white-space:nowrap}
.split-block h2{border:none}
.split-rule{width:46px;height:2px;background:var(--white);margin:12px 0 20px}
.split-block p{font-size:13px;line-height:21.7px;text-align:justify}
.split-btn{width:121px;height:40px;margin-top:27px}
.split-btn.alt{background:#808080}
.center-badge{left:499px;top:994px;width:200px;height:200px;border-radius:50%;background:var(--white);box-shadow:0 0 0 6px rgba(255,255,255,.35);display:flex;align-items:center;justify-content:center;text-align:center;font-family:"Jost",sans-serif;font-weight:500;font-size:22px;line-height:1.2;color:var(--orange)}

/* reviews */
.review{background:var(--white);border:2px solid #e6e6e6;font-size:13.5px;line-height:25px;text-align:justify}
.review .quote{float:left;font-family:"Jost",sans-serif;font-size:80px;line-height:60px;height:42px;color:#c8c8c8;margin-right:14px}
.review .who{font-family:"Jost",sans-serif;color:var(--orange);font-size:19px;margin-top:10px}
.review-side{top:1453px;height:262px;padding:52px 30px 0}
.review-main{left:403px;top:1438px;width:411px;height:292px;padding:40px 26px 0;z-index:2;box-shadow:0 2px 10px rgba(0,0,0,.15);border-color:#ddd}
.dots{left:580px;top:1768px;display:flex;gap:6px;align-items:center}
.dots i{width:8px;height:8px;border-radius:50%;background:#cfcfcf}
.dots i.on{width:11px;height:11px;background:var(--orange)}

/* contact */
.contact{left:0;top:1836px;width:1200px;height:476px;background:var(--light)}
.field{background:var(--white);border:1px solid #d6d6d6;border-radius:3px;font-size:11px;color:#333;padding:12px 12px}
.submit{left:547px;top:2215px;width:106px;height:39px}

/* footer */
.footer{left:0;top:2312px;width:1200px;height:205px;background:var(--black);color:var(--white)}
.footer-links{left:0;top:2349px;width:1200px;text-align:center;font-size:14px}
.footer-links span{margin:0 12px;color:#ccc}
.social{left:507px;top:2401px;display:flex;gap:9px}
.social i{width:30px;height:30px;border-radius:50%;background:var(--white)}
.social i.on{background:var(--orange)}
.copy{left:0;top:2462px;width:1200px;text-align:center;font-size:11px;color:#ddd}
</style>
</head>
<body>

<div class="abs topbar">
  <div class="item"><span class="dot"><svg width="10" height="10" viewBox="0 0 10 10"><path d="M2 1l2 2-1 1.2a6 6 0 002.8 2.8L7 6l2 2-1.3 1.3C4.5 9.3.7 5.5.7 2.3z" fill="#fff"/></svg></span>Call Us : (555) 010-2468</div>
  <div class="item"><span class="dot"><svg width="10" height="8" viewBox="0 0 10 8"><rect x="0" y="0" width="10" height="8" fill="#fff"/><path d="M0 0l5 4 5-4" stroke="#5c5c5c" fill="none"/></svg></span>Mail Us : info@pinegladeloft.com</div>
</div>

<div class="abs brand"><span class="mark"></span><span class="name">The Pine<br>Glade Loft</span></div>

<nav class="abs nav">
  <a class="active">HOME</a><a>FOR BUSINESS</a><a>FOR WORKERS</a><a>REVIEWS</a>
</nav>
<div class="abs btn nav-cta">Get In Contact</div>

<div class="abs hero" role="img" aria-label="Photo of three colleagues reviewing documents at an office desk"></div>
<div class="abs hero-caption"><h1>Ullamco Laboris Nisi Ut<br>Aliquip Commodo Consequat</h1></div>
<div class="abs btn hero-btn">Contact Now</div>

<h2 class="abs heading section-title" style="top:680px">Welcome to <span>The Pine Glade Loft</span></h2>
<div class="abs divider" style="top:745px"><i></i></div>
<p class="abs lead" style="top:785px">Lorem ipsum dolor sit amet, consectetur adipiscing elit, sed do eiusmod tempor incididunt ut labore et dolore magna aliqua. Ut enim ad minim veniam, quis nostrud exercitation ullamco laboris nisi ut aliquip ex ea commodo consequat. Duis aute irure dolor in reprehenderit in voluptate velit esse cillum dolore eu fugiat nulla pariatur. Excepteur sint occaecat cupidatat non proident, sunt in culpa qui officia perspiciatis unde omnis iste natus error sit voluptatem</p>

<div class="abs split" role="img" aria-label="Muted photo of an office meeting behind the business panel"></div>
<svg class="abs split-orange" width="1200" height="370" viewBox="0 0 1200 370" role="img" aria-label="Orange-tinted photo of people working behind the workers panel">
  <defs><linearGradient id="og" x1="0" x2="1"><stop offset="0" stop-color="#f28a1c"/><stop offset="1" stop-color="#e87500"/></linearGradient></defs>
  <polygon points="688,0 1200,0 1200,370 503,370" fill="url(#og)"/>
</svg>

<div class="abs split-block" style="left:89px;top:955px">
  <h2><svg width="36" height="32" viewBox="0 0 36 32"><rect x="2" y="16" width="7" height="16" fill="#fff"/><rect x="13" y="10" width="7" height="22" fill="#fff"/><rect x="24" y="4" width="7" height="28" fill="#fff"/></svg>FOR BUSINESS</h2>
  <div class="split-rule"></div>
  <p>Sed ut perspiciatis unde omnis iste natus error sit voluptatem accusantium doloremque laudantium, totam rem aperiam, eaque ipsa quae ab illo inventore veritatis et quasi architecto beatae vitae dicta sunt explicabo. Nemo enim ipsam voluptatem quia voluptas sit aspernatur aut odit aut fugit, sed quia consequuntur magni dolores eos</p>
  <div class="btn split-btn">Learn More</div>
</div>

<div class="abs split-block" style="left:753px;top:955px">
  <h2><svg width="36" height="32" viewBox="0 0 36 32"><circle cx="18" cy="7" r="5" fill="#fff"/><rect x="13" y="14" width="10" height="18" fill="#fff"/><circle cx="6" cy="11" r="4" fill="#fff"/><rect x="2" y="17" width="8" height="13" fill="#fff"/><circle cx="30" cy="11" r="4" fill="#fff"/><rect x="26" y="17" width="8" height="13" fill="#fff"/></svg>FOR WORKERS</h2>
  <div class="split-rule"></div>
  <p>Sed ut perspiciatis unde omnis iste natus error sit voluptatem accusantium doloremque laudantium, totam rem aperiam, eaque ipsa quae ab illo inventore veritatis et quasi architecto beatae vitae dicta sunt explicabo. Nemo enim ipsam voluptatem quia voluptas sit aspernatur aut odit aut fugit, sed quia consequuntur magni dolores eos</p>
  <div class="btn split-btn alt">Learn More</div>
</div>

<div class="abs center-badge">The Pine<br>Glade Loft</div>

<h2 class="abs heading section-title" style="top:1325px">Client <span>Reviews</span></h2>
<div class="abs divider" style="top:1388px"><i></i></div>

<div class="abs review review-side" style="left:129px;width:420px">
  <span class="quote">&ldquo;</span>Ut enim ad minim veniam, quis nostrud exercitation ullamco laboris nisi ut aliquip ex ea commodo consequat. Duis aute irure dolor in reprehenderit in voluptate velit esse cillum dolore eu fugiat nulla pariatur. Excepteur sint occaecat cupidatat
  <div class="who">- Marit V.</div>
</div>
<div class="abs review review-side" style="left:651px;width:420px;padding-left:30px">
  <span class="quote">&ldquo;</span>On the other hand, we denounce with righteous indignation and dislike men who are so beguiled and demoralized by the charms of pleasure of the moment, so blinded by desire, that they cannot foresee the pain and trouble that are bound to ensue
  <div class="who">- Sanne L.</div>
</div>
<div class="abs review review-main">
  <span class="quote">&ldquo;</span>At vero eos et accusamus et iusto odio dignissimos ducimus qui blanditiis praesentium voluptatum deleniti atque corrupti quos dolores et quas molestias excepturi sint occaecati cupiditate non provident, similique sunt in culpa qui officia deserunt mollitia animi, id est laborum et dolorum fuga. Et harum quidem rerum facilis est et expedita distinctio. Nam libero tempore, cum soluta
  <div class="who">- Joost D.</div>
</div>
<div class="abs dots"><i></i><i class="on"></i><i></i></div>

<div class="abs contact"></div>
<h2 class="abs heading section-title" style="top:1882px">Quick <span>Contact</span></h2>
<div class="abs divider" style="top:1945px"><i></i></div>
<p class="abs lead" style="top:1990px;left:120px;width:960px">Duis aute irure dolor in reprehenderit in voluptate velit esse cillum dolore eu fugiat nulla pariatur. Excepteur sint occaecat cupidatat non proident, sunt in culpa qui officia deserunt mollit anim id est laborum magni dolores eos qui ratione voluptatem sequi nesciunt</p>
<div class="abs field" style="left:89px;top:2062px;width:331px;height:39px">Name</div>
<div class="abs field" style="left:433px;top:2062px;width:332px;height:39px">Email</div>
<div class="abs field" style="left:779px;top:2062px;width:332px;height:39px">Phone</div>
<div class="abs field" style="left:89px;top:2118px;width:1022px;height:79px">Message</div>
<div class="abs btn submit">Submit</div>

<div class="abs footer"></div>
<div class="abs footer-links">Home<span>/</span>For Business<span>/</span>For Workers<span>/</span>Reviews<span>/</span>Contact Us</div>
<div class="abs social" aria-label="Social links"><i class="on"></i><i></i><i></i><i></i><i></i></div>
<div class="abs copy">Copyright © 2017 The Pine Glade Loft. All Rights Reserved</div>

</body>
</html>
```